harvest Ahead Book Cover Design for real estate investment book

I am looking for a Book Cover design for my new book. I would like designs for a hardcover, softcover and Lumora book.

The book deals with real estate and mortgage investments. Looking for a clean, bright simple design. Want to cover to be White with big RED letters. See "Leading from Wonder" book for an example ... see attached.

Target Market(s)

Affluent people with money looking for investment solutions.

Industry/Entity Type

Financial Service

Font styles to use
Serif

Requirements
Must have
• Bright clean design that will be appealing to affluent people.
• Title: harvest AHEAD
• Subtitle: The quiet path to thriving through property holdings
• subsubtitle: Secrets Your Fund Manager Keeps Quiet About...
• Author: Ned Garroway
• My Picture on the inside cover or on the back cover
• Book Description, Author description
Nice to have
• Focus on the Front cover look and feel first. Then we can look at the inside flaps and back cover. I will need to send you text. This is for the full cover. Front. Back. Spine. Inside flaps fro hardcover.

```html
<!DOCTYPE html>
<html lang="en">
<head>
<meta charset="utf-8">
<title>harvest AHEAD — Ned Garroway</title>
<link href="https://fonts.googleapis.com/css2?family=Montserrat:wght@700;800;900&family=Josefin+Sans:wght@400;600&display=swap" rel="stylesheet">
<style>
  :root {
    --page: #f3f3f3;
    --cover: #ffffff;
    --red: #c4161c;
    --ink: #111111;
    --suit-light: #d3d3d3;
    --suit-dark: #161616;
  }
  * { margin: 0; padding: 0; box-sizing: border-box; }
  html, body {
    width: 1200px; height: 1200px; overflow: hidden;
    background: var(--page);
  }
  .book-cover {
    position: absolute;
    left: 222px; top: 34px;
    width: 756px; height: 1132px;
    background: var(--cover);
    overflow: hidden;
  }
  .title {
    position: absolute;
    left: 0; top: 0;
    width: 756px; height: 420px;
  }
  .title text {
    font-family: "Montserrat", sans-serif;
    font-weight: 900;
    fill: var(--red);
  }
  .subtitle {
    position: absolute;
    left: 60px; top: 400px;
    width: 636px;
    text-align: center;
    font-family: "Josefin Sans", sans-serif;
    font-weight: 400;
    font-size: 29px;
    line-height: 34px;
    letter-spacing: 1px;
    text-transform: uppercase;
    color: var(--ink);
  }
  .tagline {
    position: absolute;
    left: 60px; top: 478px;
    width: 636px;
    text-align: center;
    font-family: "Josefin Sans", sans-serif;
    font-weight: 600;
    font-size: 14px;
    letter-spacing: 1px;
    text-transform: uppercase;
    color: var(--red);
  }
  .cover-art {
    position: absolute;
    left: 134px; top: 520px;
    width: 490px; height: 612px;
    background: linear-gradient(180deg, var(--suit-light) 0%, var(--suit-light) 12%, #2a2a2a 30%, var(--suit-dark) 100%);
  }
  .author {
    position: absolute;
    left: 14px; top: 1064px;
    font-family: "Montserrat", sans-serif;
    font-weight: 800;
    font-size: 48px;
    line-height: 56px;
    white-space: nowrap;
  }
  .author-first { color: var(--ink); }
  .author-last { color: #ffffff; }
  .author-rule {
    position: absolute;
    left: 14px; top: 1124px;
    width: 340px; height: 4px;
    background: linear-gradient(90deg, var(--red) 0%, var(--red) 70%, rgba(196,22,28,0) 100%);
  }
</style>
</head>
<body>
  <main class="book-cover">
    <svg class="title" viewBox="0 0 756 420" aria-label="harvest AHEAD">
      <text x="22" y="208" font-size="158" textLength="712" lengthAdjust="spacingAndGlyphs">HARVEST</text>
      <text x="116" y="362" font-size="158" textLength="524" lengthAdjust="spacingAndGlyphs">AHEAD</text>
    </svg>

    <p class="subtitle">The quiet path to thriving<br>through property holdings</p>
    <p class="tagline">Secrets Your Fund Manager Keeps Quiet About...</p>

    <div class="cover-art" role="img" aria-label="Illustration of a headless man's black three-piece suit with a tie made of folded dollar bills and a red pocket square"></div>

    <p class="author"><span class="author-first">Ned</span> <span class="author-last">Garroway</span></p>
    <div class="author-rule"></div>
  </main>
</body>
</html>
```